Holvern Cabinets Quality Custom Built Kitchens, Vanity Units, Robes ect

Hi,
Was after a new design for our business cards,
we are a cabinet making business and pride ourselves in quality custom built Kitchens, Vanity units, robes ect.
we have been around for over 20 years and we are trying to modernize our card logo.
Looking for something eye catching, bold and exciting
family ran and operated business, we work with builders and also have a large private clientel.

Thanks

Industry/Entity Type

Business

Contact Information for Business Card

Holvern Cabinets

Font styles to use
Serif
Script

Requirements
Must have
• Marisol 0461937254 hvcabinets@mailvento.com
• Po Box 2786
• 5C Larkspur Court Kelmarsh Vic 3917
• Phone (03)52896407 Fax (03) 52896931
Nice to have
• Quality Custom Built Kitchens & Vanity Units

```html
<!DOCTYPE html>
<html lang="en">
<head>
<meta charset="utf-8">
<title>Holvern Cabinets – Business Card</title>
<link rel="stylesheet" href="https://fonts.googleapis.com/css2?family=Open+Sans:wght@400;600&family=Ubuntu:wght@700&display=swap">
<style>
  :root {
    --maroon: #6a3b3f;
    --ink: #161616;
    --paper: #ffffff;
    --backdrop: #ece7e1;
    --rule: #2a2a2a;
  }
  * { margin: 0; padding: 0; box-sizing: border-box; }
  html, body { width: 1200px; height: 900px; overflow: hidden; }
  body {
    background: var(--backdrop);
    font-family: "Open Sans", Arial, sans-serif;
    color: var(--ink);
    position: relative;
  }
  .card {
    position: absolute;
    left: 240px;
    width: 720px;
    height: 400px;
    background: var(--paper);
    border-radius: 24px;
    overflow: hidden;
    box-shadow: 0 6px 18px rgba(0,0,0,0.12);
  }
  .card--front { top: 40px; }
  .card--back { top: 465px; }
  .card__shapes { position: absolute; inset: 0; }

  .brand { position: absolute; text-align: right; }
  .brand__name {
    font-family: "Ubuntu", Arial, sans-serif;
    font-weight: 700;
    color: var(--ink);
    letter-spacing: 1px;
    line-height: 1;
    white-space: nowrap;
  }
  .brand__tagline {
    font-family: "Ubuntu", Arial, sans-serif;
    font-weight: 700;
    color: var(--ink);
    white-space: nowrap;
  }
  .card--front .brand { left: 0; right: 0; top: 130px; text-align: center; }
  .card--front .brand__name { font-size: 56px; }
  .card--front .brand__tagline { font-size: 18px; margin-top: 8px; }

  .address {
    position: absolute;
    left: 110px; right: 40px; bottom: 16px;
    color: var(--paper);
    font-size: 19px;
    letter-spacing: 0.5px;
    text-align: center;
    white-space: nowrap;
  }

  .contact-name {
    position: absolute;
    left: 82px; top: 22px;
    font-size: 34px;
    font-weight: 400;
  }
  .contact-list { position: absolute; left: 82px; list-style: none; font-size: 20px; line-height: 1; }
  .contact-list li { display: flex; align-items: center; gap: 10px; height: 28px; }
  .contact-list svg { width: 18px; height: 18px; flex: none; }
  .contact-list--mobile { top: 78px; }
  .contact-list--office { top: 158px; }

  .card--back .brand { right: 50px; top: 262px; }
  .card--back .brand__name { font-size: 54px; }
  .card--back .brand__tagline { font-size: 18px; margin-top: 8px; }
</style>
</head>
<body>

  <section class="card card--front" aria-label="Card front">
    <svg class="card__shapes" viewBox="0 0 720 400" aria-hidden="true">
      <path fill="var(--maroon)" d="M0,400 V300 C30,335 70,345 130,345 H640 C685,345 710,332 720,315 V400 Z"/>
    </svg>
    <div class="brand">
      <div class="brand__name">Holvern Cabinets</div>
      <div class="brand__tagline">Quality Custom Built Kitchens &amp; Vanity Units</div>
    </div>
    <p class="address">Po Box 2786 5C Larkspur Court Kelmarsh Vic 3917</p>
  </section>

  <section class="card card--back" aria-label="Card back">
    <svg class="card__shapes" viewBox="0 0 720 400" aria-hidden="true">
      <path fill="var(--maroon)" d="M0,0 H40 Q70,200 40,400 H0 Z"/>
      <path fill="var(--maroon)" d="M720,90 Q695,150 705,220 Q712,260 720,280 Z"/>
      <line x1="225" y1="52" x2="690" y2="52" stroke="var(--rule)" stroke-width="1.5"/>
    </svg>

    <h1 class="contact-name">Marisol</h1>

    <ul class="contact-list contact-list--mobile">
      <li>
        <svg viewBox="0 0 18 18" aria-label="Mobile"><rect x="4" y="1" width="10" height="16" rx="2" fill="none" stroke="var(--maroon)" stroke-width="2"/><circle cx="9" cy="14" r="1" fill="var(--maroon)"/></svg>
        0461937254
      </li>
    </ul>

    <ul class="contact-list contact-list--office">
      <li>
        <svg viewBox="0 0 18 18" aria-label="Fax"><rect x="4" y="1" width="10" height="5" fill="var(--maroon)"/><rect x="1" y="6" width="16" height="7" rx="2" fill="var(--maroon)"/><rect x="4" y="11" width="10" height="6" fill="var(--paper)" stroke="var(--maroon)" stroke-width="1.5"/></svg>
        (03) 52896931
      </li>
      <li>
        <svg viewBox="0 0 18 18" aria-label="Phone"><path d="M4,1 L7,1 L8,5 L6,7 C7,10 8,11 11,12 L13,10 L17,11 L17,14 C17,16 15,17 13,17 C7,16 2,11 1,5 C1,3 2,1 4,1 Z" fill="var(--maroon)"/></svg>
        (03)52896407
      </li>
      <li>
        <svg viewBox="0 0 18 18" aria-label="Email"><rect x="1" y="4" width="16" height="11" fill="none" stroke="var(--maroon)" stroke-width="1.6"/><path d="M1,4 L9,11 L17,4" fill="none" stroke="var(--maroon)" stroke-width="1.6"/></svg>
        hvcabinets@mailvento.com
      </li>
    </ul>

    <div class="brand">
      <div class="brand__name">Holvern Cabinets</div>
      <div class="brand__tagline">Quality Custom Built Kitchens &amp; Vanity Units</div>
    </div>
  </section>

</body>
</html>
```